Brell Harbor Company Business Cards

Front and Back Business Card - logo and text setup - cool design. I need workable photoshop or illustrator files so I can setup each employee card with design that is created
Updates

Hi everyone, thank you for the great entries. Please no more white and blue cards - there are so many already - black and silver only now please. thanks!

Target Market(s)

Construction Industry - Facility Managers

Industry/Entity Type

Construction

Contact Information for Business Card

I really like contemporary simplistic looks - clean neat....not opposed to seeing some black backrounds

Requirements
Must have
• Logo/website address with design on front only - www.brellharbor-example.com (logo attached)
• Back:
• Name/Title/Company Address/Phone/email address
Nice to have
• Cool design
Should not have
• Nothing gimmicky like Fire or Water - since we are a Fire Protection company - it has all been done

```html
<!DOCTYPE html>
<html lang="en">
<head>
<meta charset="utf-8">
<title>Brell Harbor Company Business Cards</title>
<link href="https://fonts.googleapis.com/css2?family=Lato:wght@400;900&family=Oswald:wght@500&display=swap" rel="stylesheet">
<style>
  :root {
    --backdrop: #2b2b2b;
    --card: #1d1d1e;
    --edge: #26467f;
    --white: #f2f2f2;
    --silver: #8a8a8c;
    --accent-red: #d8462f;
    --accent-blue: #2f55a0;
  }
  * { margin: 0; padding: 0; box-sizing: border-box; }
  html, body {
    width: 1200px; height: 895px; overflow: hidden;
    background: var(--backdrop);
    font-family: "Lato", Arial, sans-serif;
  }
  .card {
    position: absolute;
    width: 525px; height: 300px;
    background: var(--card);
    border-radius: 14px;
    border-bottom: 4px solid var(--edge);
    box-shadow: 0 18px 40px rgba(0,0,0,.55);
    color: var(--white);
  }
  .card--front { left: 60px; top: 140px; }
  .card--back  { left: 615px; top: 455px; }

  .front__logo {
    position: absolute; left: 0; right: 0; top: 92px;
    text-align: center;
    font-family: "Lato", Arial, sans-serif;
    font-weight: 900; font-size: 54px; letter-spacing: -1px;
    color: var(--silver);
  }
  .front__web {
    position: absolute; left: 0; right: 0; bottom: 34px;
    text-align: center; font-size: 15px; letter-spacing: .5px;
  }
  .domain--blue { color: var(--accent-blue); }
  .domain--red { color: var(--accent-red); }

  .back__identity {
    position: absolute; left: 44px; top: 104px; width: 205px;
  }
  .back__name {
    font-family: "Oswald", "Arial Narrow", sans-serif;
    font-weight: 500; font-size: 33px; line-height: 1;
    text-transform: uppercase; letter-spacing: .5px;
  }
  .back__title {
    margin-top: 6px; font-size: 16px; color: var(--accent-red); letter-spacing: .5px;
  }
  .back__divider {
    position: absolute; left: 262px; top: 96px;
    width: 2px; height: 64px; background: var(--white); opacity: .8;
  }
  .back__contacts {
    position: absolute; left: 282px; top: 92px; list-style: none;
    font-size: 14px; line-height: 24px;
  }
  .back__contacts li { display: flex; align-items: center; gap: 9px; }
  .back__contacts svg { width: 13px; height: 13px; flex: none; }
  .back__address {
    position: absolute; left: 0; right: 0; bottom: 30px;
    text-align: center; font-size: 15px; letter-spacing: .4px;
  }
</style>
</head>
<body>
  <section class="card card--front" aria-label="Card front">
    <div class="front__logo">Brell Harbor</div>
    <div class="front__web">www.<span class="domain--blue">brell</span><span class="domain--red">harbor-example</span>.com</div>
  </section>

  <section class="card card--back" aria-label="Card back">
    <div class="back__identity">
      <div class="back__name">Dana Whitfield</div>
      <div class="back__title">Founder &amp; CEO</div>
    </div>
    <div class="back__divider"></div>
    <ul class="back__contacts">
      <li>
        <svg viewBox="0 0 14 14" aria-hidden="true"><rect x="3.5" y="1" width="7" height="12" rx="1.5" fill="none" stroke="var(--accent-red)" stroke-width="1.6"/></svg>
        000 000 0000
      </li>
      <li>
        <svg viewBox="0 0 14 14" aria-hidden="true"><rect x="1" y="3" width="12" height="8" fill="none" stroke="var(--accent-red)" stroke-width="1.5"/><path d="M1 3l6 5 6-5" fill="none" stroke="var(--accent-red)" stroke-width="1.5"/></svg>
        <span>info@<span class="domain--blue">brell</span><span class="domain--red">harbor-example</span>.com</span>
      </li>
      <li>
        <svg viewBox="0 0 14 14" aria-hidden="true"><circle cx="7" cy="6" r="4.5" fill="none" stroke="var(--accent-red)" stroke-width="1.6"/><path d="M4 10l-2 3" stroke="var(--accent-red)" stroke-width="1.6"/></svg>
        <span>www.<span class="domain--blue">brell</span><span class="domain--red">harbor-example</span>.com</span>
      </li>
    </ul>
    <div class="back__address">4820 Larkspur Avenue, Suite 120, Fairmont, NE 68000</div>
  </section>
</body>
</html>
```